Brightwell Wiring Needs A Logo Design

We need a logo for my new company based out of Sacramento, Ca called Brightwell Wiring. The name says it all, my electrical contracting business provides "Brightwell Craftsman Work" I'm open to any colors that pop and customers to say Wow. I would love to print my cards on metal.

Contact Information for Business Card

The card needs to have as follows
Name of company: Brightwell Wiring
My Name: Marco Delvane
Phone # 916-555-0147
CL# 4873920
Email: brightwellwiring@mailtorva.com
and a slogan that represent "BRIGHTWELL"

Requirements
Must have
• The card needs to have as follows
• Name of company: Brightwell Wiring
• My Name : Marco Delvane
• Phone # 916-555-0147
• CL# 4873920
• Email: brightwellwiring@mailtorva.com
• and a slogan that represent "BRIGHTWELL"
Nice to have
• popping colors
• electrical Arcing

```html
<!DOCTYPE html>
<html lang="en">
<head>
<meta charset="utf-8">
<title>Brightwell Wiring – Business Card</title>
<link rel="stylesheet" href="https://fonts.googleapis.com/css2?family=Open+Sans:ital,wght@0,400;0,600;0,700;1,600;1,700&display=swap">
<style>
  :root {
    --stage: #000000;
    --card: #2f3033;
    --card-edge: #35363a;
    --blue: #1a8bb3;
    --orange: #f0a016;
    --ink: #f1f1f1;
    --rule: #45464a;
  }
  * { box-sizing: border-box; margin: 0; padding: 0; }
  html, body {
    width: 1200px; height: 900px; overflow: hidden;
    background: var(--stage);
    font-family: "Open Sans", Arial, sans-serif;
  }
  .stage { position: relative; width: 1200px; height: 900px; }
  .card {
    position: absolute; top: 271px;
    width: 457px; height: 281px;
    background: var(--card);
    border-radius: 14px;
    box-shadow: inset 0 0 0 1px var(--card-edge);
  }
  .card--front { left: 137px; }
  .card--back { left: 626px; }

  .brand-name {
    position: absolute;
    color: var(--blue);
    font-weight: 700;
    line-height: 1.05;
  }
  .card--front .brand-name {
    left: 56px; top: 100px; width: 140px;
    font-size: 26px;
  }
  .divider {
    position: absolute; left: 211px; top: 74px;
    width: 1px; height: 136px; background: var(--rule);
  }
  .contact { position: absolute; left: 244px; top: 93px; }
  .contact__name {
    font-size: 16.5px; font-weight: 600; margin-bottom: 16px;
  }
  .contact__name .first { color: var(--blue); }
  .contact__name .last { color: var(--orange); }
  .contact__list { list-style: none; }
  .contact__item {
    display: flex; align-items: center; gap: 9px;
    color: var(--ink); font-size: 12.5px; height: 19px;
  }
  .contact__icon { width: 8px; height: 10px; fill: var(--orange); flex: none; }
  .slogan {
    position: absolute; left: 0; right: 0; top: 227px;
    text-align: center; font-size: 15.5px; font-weight: 700; font-style: italic;
  }
  .slogan .lead { color: var(--blue); }
  .slogan .rest { color: var(--orange); }

  .card--back .brand-mark {
    position: absolute; left: 50%; top: 112px; transform: translateX(-50%);
    display: flex; align-items: center; gap: 14px; white-space: nowrap;
  }
  .brand-mark__square { width: 26px; height: 26px; background: var(--orange); }
  .card--back .brand-name { position: static; font-size: 34px; }
</style>
</head>
<body>
<main class="stage">
  <section class="card card--front">
    <div class="brand-name">Brightwell Wiring</div>
    <div class="divider"></div>
    <div class="contact">
      <p class="contact__name"><span class="first">Marco</span> <span class="last">Delvane</span></p>
      <ul class="contact__list">
        <li class="contact__item">
          <svg class="contact__icon" viewBox="0 0 10 10"><path d="M2 0.5l2 2-1 1.2c.6 1.3 1.5 2.2 2.8 2.8L7 5.5l2 2-1.2 1.8C4.5 9.3.7 5.5.7 2.2z"/></svg>
          916-555-0147
        </li>
        <li class="contact__item">
          <svg class="contact__icon" viewBox="0 0 8 10"><path d="M1.5 0h5a1 1 0 0 1 1 1v8a1 1 0 0 1-1 1h-5a1 1 0 0 1-1-1V1a1 1 0 0 1 1-1zm.5 1.3v6.2h4V1.3z"/></svg>
          4873920
        </li>
        <li class="contact__item">
          <svg class="contact__icon" viewBox="0 0 10 8" style="width:9px;height:8px"><path d="M0 1h10v6H0z M0 1l5 3.5L10 1" stroke="#2f3033" stroke-width="0.8"/></svg>
          brightwellwiring@mailtorva.com
        </li>
      </ul>
    </div>
    <p class="slogan"><span class="lead">Brightwell</span> <span class="rest">Craftsman Work</span></p>
  </section>

  <section class="card card--back">
    <div class="brand-mark">
      <span class="brand-mark__square"></span>
      <span class="brand-name">Brightwell Wiring</span>
    </div>
  </section>
</main>
</body>
</html>
```